Talvera Web site

Talvera is a trade name for Dresgan enterprises llc, would like Dresgan mentioned but not prominent.

Use current logo to base colors and look/feel of website. Modern trendy look.

Talvera Technical Services - "Irrevocably committed to your success"

Website design for a nation wide service based company

Networking, AV, access control, automation, EAS, project management, consulting, electrical, design, service staffing

Hostwick hosts our URL's

Questions-
Who owns the content once accepted.
How is the content delivered to build site
How do we adjust. or add to content once published

Target Market(s)

commercial and retail technical services. IE, we provide technical services for retail and commercial vertical markets

Industry/Entity Type

Trade

Coding

Coded - Design and coding required

Number of Pages Required

5+ page

Font styles to use
Sans Serif

Colors
3276b5

Requirements
Must have
• Pages-
• About/info, contact, services, customers log in portal, social media links
• links to outside web based software portals
• Call through (call me) links

```html
<!DOCTYPE html>
<html lang="en">
<head>
<meta charset="utf-8">
<title>Talvera Technical Services</title>
<link href="https://fonts.googleapis.com/css2?family=Open+Sans:wght@300;400;600;700;800&display=swap" rel="stylesheet">
<style>
:root{
  --blue:#3276b5;
  --blue-dark:#23609a;
  --green:#3a9a2e;
  --ink:#222;
  --muted:#8a8a8a;
  --grey-band:#eeeeee;
  --footer:#1f1f1f;
  --footer-2:#181818;
  --footer-text:#e8e8e8;
  --footer-muted:#9a9a9a;
}
*{box-sizing:border-box;margin:0;padding:0}
html,body{width:856px;height:1200px;overflow:hidden}
body{position:relative;font-family:"Open Sans",Arial,sans-serif;color:var(--ink);background:#fff}
.abs{position:absolute}

/* header */
.site-header{position:absolute;left:0;top:0;width:856px;height:80px;background:linear-gradient(#3a80c0,var(--blue))}
.brand{position:absolute;left:78px;top:0;width:249px;height:88px;background:#fff;box-shadow:0 3px 6px rgba(0,0,0,.18);display:flex;align-items:center;padding-left:22px;gap:10px}
.brand-dot{width:40px;height:40px;border-radius:50%;background:var(--blue)}
.brand-name{font-size:30px;font-weight:800;color:var(--blue);letter-spacing:.5px}
.main-nav a{position:absolute;top:31px;font-size:12.5px;color:#fff;text-decoration:none}
.main-nav .is-active{left:452px;top:30px;width:51px;height:22px;line-height:22px;text-align:center;background:var(--green);border-radius:2px;font-weight:700}

/* hero */
.hero{position:absolute;left:0;top:80px;width:856px;height:394px;background:linear-gradient(90deg,#ececec,#f7f7f7 45%,#f2f2f2)}
.hero-photo{position:absolute;left:410px;top:0;width:446px;height:394px;background:linear-gradient(90deg,rgba(245,245,245,1) 0%,#b9b9b9 25%,#6c6f74 55%,#9ea2a7 85%,#d4d4d4 100%)}
.hero-title{position:absolute;left:78px;top:168px;font-size:30px;line-height:32px;font-weight:400;font-variant:small-caps;color:#222;letter-spacing:.2px}
.rule-label{position:absolute;left:79px;top:246px;width:325px;height:16px;text-align:center}
.rule-label::before{content:"";position:absolute;left:0;right:0;top:8px;border-top:1px dashed #aaa}
.rule-label span{position:relative;background:#f0f0f0;padding:0 7px;font-size:13px;font-variant:small-caps;color:#888}
.service-grid{position:absolute;left:79px;top:271px;width:326px;display:grid;grid-template-columns:repeat(3,107px);grid-auto-rows:47px;gap:2px}
.service-tile{background:#fff;border:1px solid #dcdcdc;display:flex;align-items:center;gap:7px;padding-left:8px;font-size:11.5px;line-height:13px;color:#333}
.service-tile.is-active{border:2px solid var(--green);color:var(--green)}
.service-tile svg{flex:none}
.more-rule{position:absolute;left:79px;top:401px;width:186px;border-top:1px dashed #aaa}
.more-btn{position:absolute;left:263px;top:387px;width:142px;height:30px}
.more-btn span{position:absolute;left:0;top:0;width:132px;height:30px;line-height:30px;text-align:center;color:#fff;font-size:12px;font-weight:600}

/* intro band */
.intro{position:absolute;left:0;top:474px;width:856px;height:256px;background:var(--grey-band)}
.sec-title{position:absolute;font-size:22px;font-weight:700;color:var(--ink);letter-spacing:-.2px}
.sec-title em{font-style:normal;color:var(--blue)}
.sec-sub{position:absolute;font-size:12.5px;color:#333}
.body-copy{position:absolute;font-size:10px;line-height:15.7px;color:var(--muted);font-weight:300}
.btn{position:absolute;width:88px;height:28px;line-height:28px;text-align:center;background:var(--blue);color:#fff;font-size:9.5px;border-radius:1px}
.ticks{position:absolute;left:464px;top:573px;list-style:none}
.ticks li{font-size:10px;color:var(--muted);font-weight:300;height:21.5px;display:flex;gap:10px;align-items:center}

/* testimonials/blog */
.avatar{position:absolute;left:80px;top:829px;width:54px;height:54px;background:linear-gradient(135deg,#c9b8a8,#e6d2c6 55%,#b86a7a)}
.quote-line{position:absolute;left:144px;top:829px;width:2px;height:98px;background:#ddd}
.quote-arrow{position:absolute;left:144px;top:852px}
.quote-name{position:absolute;left:163px;top:829px;font-size:10px;color:#1d5ea0}
.quote-name small{font-size:9px;color:var(--muted)}
.blog-thumb{position:absolute;left:457px;top:828px;width:53px;height:53px;background:linear-gradient(135deg,#1b2b4a,#2e4f86 50%,#0f1a2b)}
.blog-title{position:absolute;left:519px;top:826px;font-size:10px;font-weight:600;color:#8a8a8a}
.blog-copy{position:absolute;left:519px;top:851px;width:260px;font-size:10px;line-height:13px;color:#8a8a8a}

/* footer */
.site-footer{position:absolute;left:0;top:958px;width:856px;height:242px;background:var(--footer)}
.foot-links{position:absolute;list-style:none}
.foot-links li{font-size:8.5px;color:var(--footer-text);height:18px}
.foot-divider{position:absolute;left:346px;top:986px;width:1px;height:110px;background:#333}
.office-h{position:absolute;left:380px;top:986px;font-size:9.5px;font-weight:700;color:#fff}
.office-addr{position:absolute;left:380px;top:1004px;font-size:8px;line-height:13px;color:var(--footer-muted)}
.office-mail{position:absolute;left:382px;top:1038px;font-size:9px;font-weight:600;color:#fff;display:flex;gap:6px;align-items:center}
.tollfree{position:absolute;left:379px;top:1064px;width:204px;height:30px;background:#151515;border-radius:3px;display:flex;align-items:center;padding-left:9px;gap:6px;color:#fff;font-size:11px;font-weight:600}
.tollfree b{font-size:12px;font-weight:600}
.partner{position:absolute;left:630px;top:1015px;display:flex;align-items:center;gap:8px;color:#5d5d5d;font-size:24px;font-weight:600;letter-spacing:1px}
.partner i{width:22px;height:22px;border-radius:50%;background:#5d5d5d;display:block}
.news-row{position:absolute;left:0;top:1110px;width:856px;height:48px;border-top:1px solid #2c2c2c;border-bottom:1px solid #2c2c2c}
.news-label{position:absolute;left:80px;top:1128px;font-size:9.5px;font-weight:600;color:#fff;display:flex;gap:8px;align-items:center}
.news-input{position:absolute;left:213px;top:1124px;width:266px;height:21px;background:#fff;border:0}
.news-go{position:absolute;left:479px;top:1124px;width:29px;height:21px;line-height:21px;text-align:center;background:var(--blue);color:#fff;font-size:9px;font-weight:700}
.social{position:absolute;left:673px;top:1125px;display:flex;gap:6px}
.social span{width:16px;height:16px;background:var(--blue);border-radius:2px;display:block}
.legal{position:absolute;top:1172px;font-size:8.5px;color:#bdbdbd}
</style>
</head>
<body>

<header class="site-header">
  <div class="brand"><i class="brand-dot"></i><span class="brand-name">Talvera</span></div>
  <nav class="main-nav">
    <a class="is-active" href="#">Home</a>
    <a href="#" style="left:534px">Information</a>
    <a href="#" style="left:637px">Services</a>
    <a href="#" style="left:720px">Contact Us</a>
  </nav>
</header>

<section class="hero">
  <div class="hero-photo" role="img" aria-label="Business person holding floating green and grey service icons in an open hand"></div>
</section>
<h1 class="hero-title">Irrevocably Committed To<br>Your Success</h1>
<div class="rule-label"><span>Our Searvices</span></div>
<div class="service-grid">
  <div class="service-tile"><svg width="22" height="22" viewBox="0 0 22 22"><circle cx="11" cy="6" r="4" fill="#888"/><rect x="4" y="11" width="14" height="10" rx="3" fill="#888"/></svg>Project<br>Management</div>
  <div class="service-tile is-active"><svg width="22" height="22" viewBox="0 0 22 22"><circle cx="8" cy="8" r="5" fill="none" stroke="#3a9a2e" stroke-width="3"/><circle cx="16" cy="16" r="4" fill="none" stroke="#3a9a2e" stroke-width="3"/></svg>Automation</div>
  <div class="service-tile"><svg width="22" height="22" viewBox="0 0 22 22" stroke="#888" stroke-width="2"><path d="M5 2v18M11 2v18M17 2v18"/><circle cx="5" cy="8" r="2.5" fill="#fff"/><circle cx="11" cy="14" r="2.5" fill="#fff"/><circle cx="17" cy="6" r="2.5" fill="#fff"/></svg>Access<br>Control</div>
  <div class="service-tile"><svg width="22" height="22" viewBox="0 0 22 22"><circle cx="11" cy="6" r="4" fill="#888"/><path d="M3 21c0-6 4-9 8-9s8 3 8 9z" fill="#888"/></svg>Consulting</div>
  <div class="service-tile"><svg width="22" height="22" viewBox="0 0 22 22"><circle cx="11" cy="9" r="6" fill="none" stroke="#888" stroke-width="3"/><path d="M3 18h16" stroke="#888" stroke-width="3"/></svg>Service<br>Staffing</div>
  <div class="service-tile"><svg width="22" height="22" viewBox="0 0 22 22"><path d="M13 2 6 12h5l-2 8 7-10h-5z" fill="#888"/></svg>Electrical</div>
</div>
<div class="more-rule"></div>
<a class="more-btn" href="#"><svg width="142" height="30" viewBox="0 0 142 30" class="abs"><path d="M0 0h132l10 15-10 15H0z" fill="var(--blue)"/></svg><span>View More Services</span></a>

<section class="intro">
</section>
<h2 class="sec-title" style="left:79px;top:516px">WELCOME TO <em>TALVERA</em></h2>
<p class="sec-sub" style="left:79px;top:543px">Technical Services</p>
<p class="body-copy" style="left:78px;top:573px;width:340px">Lorem ipsum dolor sit amet, conisectetur adipiscing elit, sed do eiusmod tempor incididunt ut laboaire et dolore magna aliqua. Ut enim ad minim veniam, quis nostrud is exaercitation ullamco laboris nisi ut aliquip ex ea commodo consequiat duis aute irure dolor in reprehenderit in voluptate velit esse cillum dolore eu fugiat nulla pariatur.</p>
<a class="btn" style="left:79px;top:670px" href="#">Read More</a>

<h2 class="sec-title" style="left:464px;top:516px">WHY CHOOSE <em>US?</em></h2>
<p class="sec-sub" style="left:464px;top:543px">Lorem ipsum dolor sit consectetur</p>
<ul class="ticks">
  <li><svg width="10" height="9" viewBox="0 0 10 9"><path d="M1 5l3 3 5-7" fill="none" stroke="var(--blue)" stroke-width="2"/></svg>Lorem ipsum dolor sit amet, consectetur adipiscing elit, sed do</li>
  <li><svg width="10" height="9" viewBox="0 0 10 9"><path d="M1 5l3 3 5-7" fill="none" stroke="var(--blue)" stroke-width="2"/></svg>Eiusmod tempor incididunt ut labore et dolore magna aliqua.</li>
  <li><svg width="10" height="9" viewBox="0 0 10 9"><path d="M1 5l3 3 5-7" fill="none" stroke="var(--blue)" stroke-width="2"/></svg>Ut enim ad minim veniam, quis nostrud exercitation ullamco</li>
  <li><svg width="10" height="9" viewBox="0 0 10 9"><path d="M1 5l3 3 5-7" fill="none" stroke="var(--blue)" stroke-width="2"/></svg>Laboris nisi ut aliquip ex ea commodo consequat.</li>
</ul>
<a class="btn" style="left:466px;top:670px" href="#">Read More</a>

<h2 class="sec-title" style="left:78px;top:752px">OUR <em>TESTIMONIALS</em></h2>
<p class="sec-sub" style="left:81px;top:779px;font-weight:600;color:#444">What people say about us?</p>
<div class="avatar" role="img" aria-label="Portrait of a smiling client"></div>
<div class="quote-line"></div>
<svg class="quote-arrow" width="10" height="16" viewBox="0 0 10 16"><path d="M1 0l8 8-8 8" fill="#fff" stroke="#ddd" stroke-width="1.5"/></svg>
<p class="quote-name">-- Daniel Reeve, <small>Talvera.</small></p>
<p class="body-copy" style="left:165px;top:854px;width:250px">Lorem ipsum dolor sit amet, consectetur adipiscing elit, sed do eiusmod tempor incididunt ut labore et dolore magna aliqua. Ut enim ad minim veniam, quis nostrud exercitation ullamco.</p>

<h2 class="sec-title" style="left:456px;top:752px">BLOG <em>POST</em></h2>
<p class="sec-sub" style="left:456px;top:779px;font-weight:600;color:#444">Latest from our Blog</p>
<div class="blog-thumb" role="img" aria-label="Dark blue financial chart screen"></div>
<p class="blog-title">Lorem ipsum dolor sit amet, consectetur adipisicing</p>
<p class="blog-copy">elit, sed do eiusmod tempor incididunt ut labore et dolore magna aliqua. Ut enim ad minim veniam, quis nostrud exercitation ullamco laboris nisi ut aliquip ex ea commodo consequat [...]</p>

<footer class="site-footer"></footer>
<ul class="foot-links" style="left:79px;top:987px">
  <li>Home</li><li>About Us</li><li>Our Services</li><li>Contact Us</li>
</ul>
<ul class="foot-links" style="left:212px;top:988px">
  <li>Networking</li><li>Access control</li><li>Automation</li><li>Project Management</li><li>Consulting</li><li>More &gt;&gt;</li>
</ul>
<div class="foot-divider"></div>
<p class="office-h">Office location :</p>
<p class="office-addr">Norland Business Center Level 4, B-Wing, Tech Park 2,<br>Harbour Road Eastfield- 402118</p>
<p class="office-mail"><svg width="13" height="9" viewBox="0 0 13 9"><rect width="13" height="9" fill="#fff"/><path d="M0 0l6.5 5L13 0" fill="none" stroke="#1f1f1f"/></svg>hello@talvera.co.uk</p>
<div class="tollfree">TOLL FREE IN US <svg width="14" height="14" viewBox="0 0 14 14"><circle cx="7" cy="7" r="6" fill="none" stroke="var(--blue)" stroke-width="1.3"/><path d="M5 4c0 3 2 5 5 5l-1 1.3C6 10 4 8 3.8 5z" fill="var(--blue)"/></svg> <b>123-555-0148</b></div>
<div class="partner"><i></i>Dresgan</div>

<div class="news-row"></div>
<p class="news-label"><svg width="14" height="14" viewBox="0 0 14 14"><circle cx="7" cy="7" r="6" fill="none" stroke="var(--blue)" stroke-width="1.3"/><rect x="4" y="5" width="6" height="4" fill="var(--blue)"/></svg>JOIN OUR NEWSLETTER</p>
<div class="news-input"></div>
<div class="news-go">GO</div>
<div class="social" aria-label="Social media links"><span></span><span></span><span></span><span></span><span></span></div>
<p class="legal" style="left:79px">Copyrights © 2015. Talvera Technical Services . All Rights Reserved</p>
<p class="legal" style="left:631px">Privacy Policy &nbsp; | &nbsp; Terms &amp; Condition</p>

</body>
</html>
```